SEO marketing site

I need a design only for an SEO/Marketing project I have in mind. I have bought the domain Brivvora.example and want to aim this project at businesses who want to push their business further. WHEN I SAY DESIGN ONLY, I MEAN NO PROGRAMMING. HOWEVER, I DO NEED THE DESIGNER TO PUT THIS SITE ONLINE. $300 IS A LOT OF MONEY FOR A TEMPLATE YOU CAN PURCHASE FOR $60 WITH SOME CUSTOMISATION.

The idea is that businesses will register with us and will be offered two different kinds of services. They can make use of our scripts to check their back links, rankings, compare with competitors and a number of other marketing tools. The other service we provide is that we offer them an SEO service at a very competitive price. We will handle social networking, link building, article submission, directory submission, social bookmarking etc etc at a reasonable monthly fee.

I qoros tram look/flat design is what I really like, and I want to give off a professional vibe. This is the kind of site I wish to go for.

JUST TO REPEAT, I NEED A DESIGN TO BE PUT ONLINE, I.E PSD TO HTML CONVERSION. MY PROGRAMMERS WILL CODE THE CLIENT AREA THEMSELVES.

Target Market(s)

Other businesses

Industry/Entity Type

Marketing

Requirements
Must have
• Qoros 8 or flat design look. Even a site, similar to makerhive, is quite attractive. I would like a killer design for the site.

```html
<!DOCTYPE html>
<html lang="en">
<head>
<meta charset="utf-8">
<title>Brivvora.example – Search Engine Marketing</title>
<link href="https://fonts.googleapis.com/css2?family=Open+Sans:wght@300;400;600&display=swap" rel="stylesheet">
<style>
  :root{
    --band-grey:#efefef;
    --white:#ffffff;
    --footer-bg:#f4f4f4;
    --bar-grey:#7d7d7d;
    --ink:#2b2b2b;
    --text:#444444;
    --muted:#666666;
    --link:#3a8fd9;
    --accent:#2bb3e6;
    --tick:#5a9e12;
    --rule:#d9d9d9;
    --btn-top:#5aa9ee;
    --btn-bottom:#3a86d6;
  }
  *{margin:0;padding:0;box-sizing:border-box}
  html,body{width:1017px;height:1200px;overflow:hidden}
  body{position:relative;background:var(--white);font-family:"Open Sans",Arial,sans-serif;color:var(--text)}
  .abs{position:absolute}
  .front{z-index:2}
  a{color:var(--link);text-decoration:underline}

  .hero{left:0;top:0;width:1017px;height:556px;background:var(--band-grey)}
  .hero-title{left:0;width:1017px;top:26px;text-align:center;font-size:32px;font-weight:400;color:var(--ink)}
  .hero-sub{left:0;width:1017px;top:75px;text-align:center;font-size:19px;font-weight:400;color:var(--text)}
  .hero-shot{left:129px;top:148px;width:440px;height:305px;border-radius:5px;
    background:linear-gradient(180deg,#d8d8d8 0,#d8d8d8 18px,#2f3033 18px,#2f3033 100%);
    box-shadow:0 18px 30px -12px rgba(0,0,0,.35)}
  .hero-shot .screen{position:absolute;left:116px;top:42px;right:6px;bottom:0;background:linear-gradient(180deg,#f7f7f7,#e9ecef)}
  .intro{left:613px;top:141px;width:275px;font-size:11.2px;line-height:18.5px;text-align:justify;color:var(--text)}
  .feature .icon{position:absolute;left:613px;width:30px;height:30px}
  .feature h3{position:absolute;left:651px;font-size:14.5px;font-weight:400;color:var(--ink)}
  .feature p{position:absolute;left:654px;width:235px;font-size:10px;line-height:14.5px;color:var(--text)}

  .monitor-title{left:127px;top:628px;font-size:33px;font-weight:400;color:var(--ink);white-space:nowrap}
  .monitor-sub{left:128px;top:684px;font-size:16px;color:var(--text)}
  .checklist{left:128px;top:719px;list-style:none}
  .checklist li{height:29px;font-size:11.7px;display:flex;align-items:center;color:var(--text)}
  .checklist svg{margin-right:19px;flex:none}
  .btn{display:flex;align-items:center;justify-content:center;color:#fff;font-size:12px;
    background:linear-gradient(180deg,var(--btn-top),var(--btn-bottom));border:1px solid #2f78c4;border-radius:3px}
  .read-more{left:129px;top:847px;width:89px;height:25px}
  .devices{left:470px;top:514px;width:420px;height:410px;z-index:1;
    background:radial-gradient(ellipse at 45% 55%,#f2f2f2 0,#e6e6e6 45%,rgba(255,255,255,0) 70%)}
  .devices .tablet{position:absolute;left:8px;top:0;width:298px;height:405px;border-radius:18px;background:#f4f4f4;border:1px solid #ddd}
  .devices .tablet-screen{position:absolute;left:30px;top:46px;width:238px;height:310px;background:linear-gradient(180deg,#33353a,#e8eaec 12%,#eef0f2)}
  .devices .phone{position:absolute;left:270px;top:66px;width:128px;height:328px;border-radius:20px;background:linear-gradient(180deg,#2b2c30,#111214)}
  .devices .phone-screen{position:absolute;left:10px;top:48px;width:108px;height:196px;background:linear-gradient(180deg,#3a3b40,#eef0f2 15%)}

  .footer{left:0;top:960px;width:1017px;height:203px;background:var(--footer-bg)}
  .col-head{font-size:12px;color:var(--text);font-weight:400}
  .col-head .brand{color:var(--accent)}
  .rule{height:1px;background:var(--rule)}
  .links{list-style:none;font-size:10px;color:var(--ink)}
  .links li{height:19.4px}
  .news-text{left:459px;top:1042px;width:215px;font-size:10px;line-height:15px;color:var(--muted)}
  .email{left:459px;top:1081px;width:195px;height:24px;border:1px solid #9a9a9a;background:#e6e6e6;font-size:10px;color:#8a8a8a;padding-left:8px;display:flex;align-items:center}
  .subscribe{left:459px;top:1119px;width:90px;height:25px;font-size:12px}
  .social{left:711px;top:1048px;display:flex;align-items:center}
  .social span{width:24px;height:20px;display:flex;align-items:center;justify-content:center;border-left:1px solid var(--rule)}
  .social span:last-child{border-right:1px solid var(--rule)}
  .contact-head{left:711px;top:1085px;font-size:12px;color:var(--accent)}
  .address{left:711px;top:1102px;font-size:10px;line-height:14.5px;color:var(--muted)}
  .bottom-bar{left:0;top:1163px;width:1017px;height:37px;background:var(--bar-grey)}
  .copyright{left:130px;top:1175px;font-size:10px;color:#fff}
</style>
</head>
<body>
  <section class="hero abs"></section>
  <h1 class="hero-title abs">Search Engine Marketing</h1>
  <p class="hero-sub abs">All the tools you need for effective optimization and better SERP rankings</p>

  <div class="hero-shot abs" role="img" aria-label="Dashboard of the marketing tools shown in a browser window"><div class="screen"></div></div>

  <p class="intro abs">Lorem Ipsum is simply dummy text of the printing and typesetting industry. Lorem Ipsum has been the industry's standard dummy text ever since the 1500s, &nbsp;<a href="#">Read More</a></p>

  <div class="feature">
    <svg class="icon" style="top:243px" viewBox="0 0 30 30"><circle cx="15" cy="15" r="15" fill="#111"/><path d="M15 8a5 5 0 0 0-3 9v2h6v-2a5 5 0 0 0-3-9zM12.5 21h5v1.6h-5z" fill="none" stroke="#fff" stroke-width="1.6"/></svg>
    <h3 style="top:248px">Classic Optimization</h3>
    <p style="top:276px">Lorem Ipsum is simply dummy text of the printing and typesetting industry. Lorem Ipsum has been.<br><a href="#">Read More</a></p>
  </div>
  <div class="feature">
    <svg class="icon" style="top:332px" viewBox="0 0 30 30"><circle cx="15" cy="15" r="15" fill="#111"/><circle cx="15" cy="15" r="7" fill="none" stroke="#fff" stroke-width="1.6"/><path d="M10 12c3 1 4 3 3 6M17 9c0 3 2 4 5 4" stroke="#fff" stroke-width="1.6" fill="none"/></svg>
    <h3 style="top:337px">The New Optimization</h3>
    <p style="top:365px">Lorem Ipsum is simply dummy text of the printing and typesetting industry. Lorem Ipsum has been.<br><a href="#">Read More</a></p>
  </div>
  <div class="feature">
    <svg class="icon" style="top:421px" viewBox="0 0 30 30"><circle cx="15" cy="15" r="15" fill="#111"/><path d="M9 15a6 6 0 0 1 10-4.5M21 15a6 6 0 0 1-10 4.5" fill="none" stroke="#fff" stroke-width="2"/><path d="M19 7v4h-4M11 23v-4h4" fill="none" stroke="#fff" stroke-width="2"/></svg>
    <h3 style="top:426px">Unique Link Building</h3>
    <p style="top:454px">Lorem Ipsum is simply dummy text of the printing and typesetting industry. Lorem Ipsum has been.<br><a href="#">Read More</a></p>
  </div>

  <div class="devices abs" role="img" aria-label="Tablet and phone showing the monitoring dashboard">
    <div class="tablet"><div class="tablet-screen"></div></div>
    <div class="phone"><div class="phone-screen"></div></div>
  </div>

  <h2 class="monitor-title abs front">Monitoring Solutions</h2>
  <p class="monitor-sub abs front">Fully Monitoring Solutions SEO Tools</p>
  <ul class="checklist abs front">
    <li><svg width="14" height="13" viewBox="0 0 14 13"><path d="M1 7l4 4 8-10" fill="none" stroke="var(--tick)" stroke-width="2.6"/></svg>Lorem Ipsum is simply dummy text of the printing</li>
    <li><svg width="14" height="13" viewBox="0 0 14 13"><path d="M1 7l4 4 8-10" fill="none" stroke="var(--tick)" stroke-width="2.6"/></svg>Lorem Ipsum is simply dummy text of the printing</li>
    <li><svg width="14" height="13" viewBox="0 0 14 13"><path d="M1 7l4 4 8-10" fill="none" stroke="var(--tick)" stroke-width="2.6"/></svg>Lorem Ipsum is simply dummy text of the printing</li>
    <li><svg width="14" height="13" viewBox="0 0 14 13"><path d="M1 7l4 4 8-10" fill="none" stroke="var(--tick)" stroke-width="2.6"/></svg>Lorem Ipsum is simply dummy text of the printing</li>
  </ul>
  <a class="btn read-more abs front" href="#" style="text-decoration:none">Read More</a>

  <footer class="footer abs"></footer>

  <h4 class="col-head abs" style="left:127px;top:1004px">About <span class="brand">Brivvora.example</span></h4>
  <div class="rule abs" style="left:127px;top:1031px;width:154px"></div>
  <ul class="links abs" style="left:130px;top:1043px">
    <li>Home</li><li>Features</li><li>Plans &amp; Pricing</li><li>Blog</li><li>Add-ons</li>
  </ul>

  <h4 class="col-head abs" style="left:323px;top:1004px">Support</h4>
  <div class="rule abs" style="left:323px;top:1031px;width:113px"></div>
  <ul class="links abs" style="left:323px;top:1046px">
    <li>Support &amp; FAQ</li><li>About Us</li><li>Jobs</li><li>SEO/SEM Knowledge Base</li>
  </ul>

  <h4 class="col-head abs" style="left:459px;top:1004px">NEWSLETTER</h4>
  <p class="news-text abs">Subscribe to our newsletter! Get productivity tips, product updates and special offers.</p>
  <div class="email abs">Your Email Address</div>
  <a class="btn subscribe abs" href="#" style="text-decoration:none">Subscribe</a>

  <h4 class="col-head abs" style="left:711px;top:1004px">STAY IN TOUCH</h4>
  <div class="rule abs" style="left:711px;top:1031px;width:210px"></div>
  <div class="social abs" aria-label="Social links">
    <span><svg width="8" height="8"><circle cx="4" cy="4" r="4" fill="var(--accent)"/></svg></span>
    <span><svg width="8" height="8"><circle cx="4" cy="4" r="4" fill="#777"/></svg></span>
    <span><svg width="8" height="8"><circle cx="4" cy="4" r="4" fill="#777"/></svg></span>
    <span><svg width="8" height="8"><circle cx="4" cy="4" r="4" fill="#777"/></svg></span>
  </div>
  <p class="contact-head abs">Contact us</p>
  <p class="address abs">Lindenweg 12<br>40-118 Harlow<br>US: +1 (555) 014 2290</p>

  <div class="bottom-bar abs"></div>
  <p class="copyright abs">Copyright © 2013. Brivvora.example</p>
</body>
</html>
```